Mandala Postcard Design

I am in need of a postcard to hand out at a Psychic Fair. I envision the card to having half-of-a Mandala (from my Facebook folder), touched up a bit to make it vibrant and bold. Others vendors will have cards w/photographic backgrounds doing yoga. I'd like mine to stand out for it's line-drawn "cartoonish" nature, solid-color nature. The wording would be my basic contact info and a short description ... something like: "Experience the Magic of Mandala Making ... Next Class will be held: (open space for writing, no lines) The art is contained in this Facebook folder. Lots to choose from, with my favorites being the stronger outlined designs.

https://www.plumeworks.example/Brightkeepers/media_set?set=a.20262926615637197.2184852941.783542196&type=3
Updates

I just uploaded a few new drawings that might work better, since they are more round. I want to minimize the white space, for instance, avoid having the left & right corners empty. Another idea could be to use 1/4 mandalas in the corners. I'm ready to make a decision. I want it to look great, but as I gain drawing experience, I'll need to update my cards. Thanks! I'm not sure if this the place for this comment, but I'll also be needing a DVD label for my tutorials, and a front page design for a mandala coloring book.

Target Market(s)

Primarily women interested in metaphysical, psychic, meditation, reiki and a basic interest in art.

Font styles to use
Serif
Sans Serif

Requirements
Should not have
• Should not be on a dark card, really should be a plain white background, it seems, in order to stand out.

```html
<!DOCTYPE html>
<html lang="en">
<head>
<meta charset="utf-8">
<title>Mandala Making Postcard</title>
<link href="https://fonts.googleapis.com/css2?family=Delius&family=Patrick+Hand&display=swap" rel="stylesheet">
<style>
  :root {
    --stage: #000000;
    --card: #ffffff;
    --ink: #1a1a1a;
    --faint: #e4e4e4;
    --orange: #f7941d;
    --yellow: #fcd116;
    --red: #ef4136;
    --mauve: #c7a4c0;
    --blue: #4f8fd6;
    --green: #1fa463;
    --purple: #7b3fa0;
  }
  * { box-sizing: border-box; margin: 0; padding: 0; }
  html, body { width: 1200px; height: 850px; overflow: hidden; background: var(--stage); }
  .stage { position: relative; width: 1200px; height: 850px; }

  .card {
    position: absolute; top: 70px; width: 552px; height: 713px;
    background: var(--card); overflow: hidden; color: var(--ink);
  }
  .card--front { left: 36px; }
  .card--back { left: 614px; }

  .headline { font-family: "Delius", sans-serif; line-height: 1; }
  .subline, .label, .site { font-family: "Patrick Hand", sans-serif; line-height: 1; }

  /* Front */
  .mandala-art {
    position: absolute; inset: 0;
    background: conic-gradient(from 20deg at 67% 18%,
      var(--orange), var(--yellow), var(--red), var(--mauve),
      var(--blue), var(--green), var(--purple), var(--red), var(--orange));
    clip-path: polygon(0 0, 552px 0, 552px 462px, 470px 462px, 420px 450px,
      320px 450px, 276px 496px, 240px 460px, 170px 420px, 110px 360px,
      40px 372px, 18px 300px, 70px 232px, 70px 140px, 0 112px);
  }
  .front-title {
    position: absolute; top: 480px; font-size: 32px; letter-spacing: 1px;
  }
  .front-title--left { left: 22px; }
  .front-title--right { left: 312px; }
  .front-sub {
    position: absolute; top: 521px; font-size: 19px; letter-spacing: 0.5px;
  }
  .front-sub--left { left: 28px; }
  .front-sub--right { left: 348px; }
  .front-swirl { position: absolute; left: 0; top: 500px; width: 552px; height: 60px; }

  .class-box {
    position: absolute; left: 22px; top: 580px; width: 506px; height: 110px;
    border: 1.5px solid var(--ink);
  }
  .class-box .label {
    position: absolute; top: -11px; left: 50%; transform: translateX(-50%);
    background: var(--card); padding: 0 8px; font-size: 19px; white-space: nowrap;
  }
  .class-box .site {
    position: absolute; bottom: -9px; left: 50%; transform: translateX(-50%);
    background: var(--card); padding: 0 8px; font-size: 17px; white-space: nowrap;
  }
  .class-box .curl {
    position: absolute; right: -12px; top: -14px; width: 26px; height: 26px;
  }

  /* Back */
  .faint-art { position: absolute; background: var(--faint); }
  .faint-art--corner {
    left: 0; top: 340px; width: 232px; height: 373px;
    clip-path: polygon(0 30px, 60px 0, 150px 40px, 232px 120px, 210px 230px,
      232px 320px, 180px 373px, 0 373px);
  }
  .faint-art--top {
    left: 318px; top: 0; width: 150px; height: 88px;
    clip-path: polygon(0 0, 150px 0, 120px 55px, 75px 88px, 30px 55px);
  }
  .stamp-box {
    position: absolute; left: 36px; top: 38px; width: 101px; height: 76px;
    border: 1.5px solid var(--ink); border-radius: 9px;
  }
  .address-line {
    position: absolute; top: 38px; width: 0; height: 148px;
    border-left: 1.5px solid #555;
  }
  .address-line--1 { left: 212px; }
  .address-line--2 { left: 252px; }
  .address-line--3 { left: 291px; }

  .vertical {
    position: absolute; bottom: 27px; writing-mode: vertical-rl;
    transform: rotate(180deg); white-space: nowrap;
  }
  .back-title { left: 272px; font-size: 25px; letter-spacing: 1px; }
  .back-sub { left: 312px; font-size: 25px; letter-spacing: 0.5px; }
  .back-name { left: 346px; font-size: 36px; letter-spacing: 1px; }
  .back-rule { position: absolute; left: 386px; top: 350px; width: 30px; height: 340px; }
  .back-visit { left: 462px; font-size: 25px; letter-spacing: 1px; }
  .back-site { left: 502px; font-size: 20px; }
</style>
</head>
<body>
<main class="stage">

  <section class="card card--front">
    <div class="mandala-art" role="img" aria-label="Half of a bold, line-drawn mandala in orange, red, mauve, blue and green"></div>

    <svg class="front-swirl" viewBox="0 0 552 60" aria-hidden="true">
      <path d="M6 48 C120 46 240 49 292 47 C282 40 276 20 286 12 C298 6 306 20 296 30 C292 38 296 46 306 47 C400 48 470 46 546 47"
            fill="none" stroke="#1a1a1a" stroke-width="1.6"/>
    </svg>

    <p class="headline front-title front-title--left">EXPERIENCE</p>
    <p class="headline front-title front-title--right">THE MAGIC</p>
    <p class="subline front-sub front-sub--left">OF MANDALA MAKING WITH</p>
    <p class="subline front-sub front-sub--right">MAREN ASHFORD</p>

    <div class="class-box">
      <span class="label">Next Class will be held:</span>
      <svg class="curl" viewBox="0 0 26 26" aria-hidden="true">
        <path d="M2 13 C2 6 8 2 14 4 C20 6 22 12 24 24" fill="#fff" stroke="#1a1a1a" stroke-width="1.5"/>
      </svg>
      <span class="site">www.BrightkeepersandDesigns.com</span>
    </div>
  </section>

  <section class="card card--back">
    <div class="faint-art faint-art--top" role="img" aria-label="Faint grey outline of a partial mandala"></div>
    <div class="faint-art faint-art--corner" role="img" aria-label="Faint grey outline of a quarter mandala"></div>

    <div class="stamp-box"></div>
    <div class="address-line address-line--1"></div>
    <div class="address-line address-line--2"></div>
    <div class="address-line address-line--3"></div>

    <p class="headline vertical back-title">EXPERIENCE THE MAGIC</p>
    <p class="subline vertical back-sub">OF MANDALA MAKING WITH</p>
    <p class="headline vertical back-name">MAREN ASHFORD</p>
    <svg class="back-rule" viewBox="0 0 30 340" aria-hidden="true">
      <path d="M16 338 C14 240 17 120 15 14 C10 10 12 2 16 4 C20 6 18 12 15 14"
            fill="none" stroke="#1a1a1a" stroke-width="1.6"/>
    </svg>

    <p class="headline vertical back-visit">VISIT MY WEBSITE AT</p>
    <p class="site vertical back-site">www.BrightkeepersandDesigns.com</p>
  </section>

</main>
</body>
</html>
```